Clothing for elderly and disabled persons business card

I have seen a design on the Pelto website with a partial hand holding a heart I would like that to be incorporated above the i in Marigold
The colours should be either soft green and pinks.
The final design should communicate care, love, easy fit comfort clothing for the frail and disabled.

Marigold
Assisted CareClothing

Target Market(s)

Nursing Homes, Elderly in care or just anyone with limited mobility

Industry/Entity Type

Clothing

Contact Information for Business Card

Marigold Assisted Care Clothing
Karen Lowther Owner Sales Consultant
Phone 0461 752 038 Fax 08 9627 4083
Email: marigoldassistedclothing@fernpost.net
Website: ?????? to be created

Requirements
Nice to have
• A hand holding a heart this must form part of the i in Marigold, instead of the dot above the i I want the hand holding the heart.

```html
<!DOCTYPE html>
<html lang="en">
<head>
<meta charset="utf-8">
<title>Marigold Assisted Care Clothing – Business Card</title>
<link rel="stylesheet" href="https://fonts.googleapis.com/css2?family=Noto+Sans:wght@400;700&display=swap">
<style>
  :root {
    --backdrop: #eeece8;
    --card: #ffffff;
    --brand-green: #2f9a4c;
    --heart-pink: #d9879a;
    --soft-pink: #f2d9de;
    --soft-green: #e3efe2;
    --text-grey: #8a8a8a;
    --name-grey: #979797;
    --card-shadow: rgba(0, 0, 0, 0.12);
  }
  * { margin: 0; padding: 0; box-sizing: border-box; }
  html, body {
    width: 1200px;
    height: 643px;
    overflow: hidden;
    background: var(--backdrop);
    font-family: "Noto Sans", Verdana, sans-serif;
  }
  .stage {
    width: 1200px;
    height: 643px;
    display: flex;
    align-items: center;
    justify-content: center;
  }
  .business-card {
    position: relative;
    width: 1050px;
    height: 600px;
    background: var(--card);
    box-shadow: 0 6px 24px var(--card-shadow);
    overflow: hidden;
  }
  .care-artwork {
    position: absolute;
    left: 110px;
    top: 50px;
    width: 520px;
    height: 390px;
    border-radius: 40px;
    background: linear-gradient(180deg, var(--soft-pink) 0%, #f7ecee 45%, var(--soft-green) 100%);
    opacity: 0.75;
  }
  .brand {
    position: absolute;
    left: 50px;
    top: 205px;
    display: flex;
    align-items: center;
    gap: 14px;
  }
  .brand-mark {
    width: 26px;
    height: 26px;
    border-radius: 50%;
    background: var(--heart-pink);
  }
  .brand-name {
    font-size: 48px;
    font-weight: 400;
    color: var(--brand-green);
    letter-spacing: 0.3px;
    white-space: nowrap;
  }
  .contact-person {
    position: absolute;
    left: 665px;
    top: 290px;
    color: var(--text-grey);
    font-size: 24px;
    line-height: 1.3;
  }
  .contact-person .person-name {
    font-size: 34px;
    font-weight: 700;
    color: var(--name-grey);
    line-height: 1.15;
  }
  .contact-person .person-role {
    font-size: 18px;
    margin-bottom: 4px;
  }
  .contact-online {
    position: absolute;
    right: 210px;
    top: 468px;
    color: var(--text-grey);
    font-size: 26px;
    line-height: 1.35;
    text-align: right;
  }
</style>
</head>
<body>
  <main class="stage">
    <article class="business-card">
      <div class="care-artwork" role="img" aria-label="Soft pink heart resting in an open hand outlined in pale green"></div>

      <div class="brand">
        <span class="brand-mark"></span>
        <span class="brand-name">Marigold Assisted Care Clothing</span>
      </div>

      <div class="contact-person">
        <p class="person-name">Karen Lowther</p>
        <p class="person-role">Owner/Sales Consultant</p>
        <p class="phone">Phone 0461 752 038</p>
        <p class="fax">Fax 08 9627 4083</p>
      </div>

      <div class="contact-online">
        <p class="email">Email marigoldassistedclothing@fernpost.net</p>
        <p class="website">Website Lorem@ipsumdolor</p>
      </div>
    </article>
  </main>
</body>
</html>
```